promotional flyer for Valtera Gym

we are after a double sided a5 leaflet to promote our gym, this is to go out to the general public to entice them into getting membership.

gym membership is £30 per month

it should also include the offer of - if you present this leaflet then there will be no joining fee

some of the features of the gym include

strength machines
cardio machines
functional area
sprung floor mat area

Target Market(s)

Adults 16+ who want to go to the gym and workout

Industry/Entity Type

Gym

Font styles to use
Other font styles liked:
• montserrat Regular

Requirements
Must have
• Clean on brand design
• use images supplied by us
Nice to have
• focus on an inclusive experience as the gym will be advertised to everyone
• should also use our "fitter, stronger, Healthier"

```html
<!DOCTYPE html>
<html lang="en">
<head>
<meta charset="utf-8">
<title>Valtera Gym – A5 Leaflet</title>
<link href="https://fonts.googleapis.com/css2?family=Montserrat:wght@400;500;600;700;800;900&display=swap" rel="stylesheet">
<style>
  :root{
    --orange:#ee5a24;
    --slate:#4b5a66;
    --ink:#3d4952;
    --white:#ffffff;
    --stage:#1f1f1f;
  }
  *{box-sizing:border-box;margin:0;padding:0}
  html,body{width:1200px;height:917px;overflow:hidden;background:var(--stage);font-family:'Montserrat',sans-serif}
  .page{position:absolute;top:64px;width:558px;height:789px;overflow:hidden;background:var(--slate)}
  .page--front{left:30px}
  .page--back{left:613px}
  .abs{position:absolute}
  .shapes{position:absolute;left:0;top:0}
  .centered{text-align:center}

  /* front header */
  .brand-mark{position:absolute;border-radius:50%;border:6px solid var(--ink)}
  .brand-name{position:absolute;font-weight:500;color:var(--ink);letter-spacing:2px;white-space:nowrap}
  .brand-tag{position:absolute;font-weight:500;color:var(--orange);letter-spacing:1.4px;white-space:nowrap}
  .contact{left:296px;width:248px;color:var(--ink)}
  .contact__line{font-weight:500;font-size:15px;line-height:21px;display:flex;align-items:center;justify-content:center;gap:5px;white-space:nowrap}
  .contact__rule{height:2px;background:var(--orange);margin:8px 14px 6px}
  .hours__title{color:var(--orange);font-weight:700;font-size:16px;line-height:22px}
  .hours__text{font-size:14px;line-height:17px;font-weight:500}

  .photo-circle{position:absolute;border-radius:50%;border:6px solid var(--orange);box-shadow:inset 0 0 0 4px var(--white)}
  .offer{left:12px;top:472px;width:290px;color:var(--orange);font-weight:600;font-size:15.5px;line-height:20px;transform:rotate(-6deg);text-align:center;white-space:nowrap;z-index:2}
  .fee-badge{left:369px;top:563px;width:136px;height:80px;background:var(--orange);border-radius:16px 16px 22px 22px;color:var(--white);font-weight:700;font-size:20px;line-height:21px;padding-top:7px;text-align:center}
  .headline{left:14px;top:556px;width:280px;color:var(--orange);font-weight:900;font-size:45px;line-height:44px;text-align:center;white-space:nowrap}
  .strapline{left:14px;top:660px;width:280px;color:var(--white);font-weight:400;font-size:22px;line-height:28px;letter-spacing:1.5px;text-align:center}
  .visit{color:var(--orange);font-weight:700;font-size:20px;letter-spacing:1.5px;display:flex;align-items:center;justify-content:center;gap:5px}
  .url{color:var(--white);font-weight:600;letter-spacing:2.6px}
  .footer-band{left:0;top:735px;width:558px;height:54px;background:var(--orange);color:var(--white);font-weight:500;font-size:14.5px;line-height:18px;text-align:center;padding-top:9px}

  /* back */
  .pill{left:79px;top:423px;width:150px;height:35px;border-radius:18px;background:var(--white);color:var(--orange);font-weight:700;font-size:19px;letter-spacing:2px;line-height:35px;text-align:center}
  .benefits{left:14px;top:467px;width:262px;list-style:none;color:var(--white);font-weight:600;font-size:15.5px;line-height:21px;text-align:center;white-space:nowrap}
  .benefits li{margin-bottom:6px}
  .dot{display:inline-block;width:7px;height:7px;border-radius:50%;background:var(--orange);margin-right:8px;vertical-align:3px}
  .dot--white{background:var(--white)}
  .features{left:277px;top:455px;width:281px;height:148px;background:var(--orange);list-style:none;color:var(--white);font-weight:600;font-size:17px;line-height:25.5px;text-align:center;padding-top:20px}
  .back-footer{left:0;top:683px;width:280px;color:var(--white);text-align:center}
  .back-footer .visit{color:var(--white);font-size:19px}
  .back-footer .url{font-size:13px;letter-spacing:2px;margin-top:2px}
  .back-footer .address{font-weight:600;font-size:11.5px;line-height:12.5px;margin-top:4px;padding-right:20px}
</style>
</head>
<body>

<!-- FRONT -->
<section class="page page--front">
  <svg class="shapes" width="558" height="789" viewBox="0 0 558 789">
    <rect x="0" y="0" width="558" height="789" fill="var(--slate)"/>
    <polygon points="0,0 558,0 558,167 0,181" fill="var(--white)"/>
    <polygon points="0,181 558,167 558,177 0,195" fill="var(--orange)"/>
  </svg>
  <svg class="shapes" width="558" height="789" viewBox="0 0 558 789" role="img" aria-label="Photo of members training on spin bikes in the cardio area">
    <defs>
      <linearGradient id="spinPhoto" x1="0" y1="0" x2="1" y2="1">
        <stop offset="0" stop-color="#5d6470"/>
        <stop offset=".5" stop-color="#2e2a2c"/>
        <stop offset="1" stop-color="#6a2a24"/>
      </linearGradient>
    </defs>
    <polygon points="0,219 558,187 558,475 0,546" fill="url(#spinPhoto)"/>
    <polygon points="0,544 558,473 558,478 0,549" fill="var(--white)"/>
  </svg>

  <div class="brand-mark" style="left:120px;top:29px;width:68px;height:68px"></div>
  <div class="brand-name" style="left:20px;top:106px;font-size:29px">VALTERA GYM</div>
  <div class="brand-tag" style="left:46px;top:143px;font-size:10px">FITTER | STRONGER | HEALTHIER</div>

  <div class="abs contact" style="top:25px">
    <div class="contact__line">
      <svg width="13" height="13" viewBox="0 0 24 24"><path d="M6.6 10.8a15 15 0 0 0 6.6 6.6l2.2-2.2a1 1 0 0 1 1-.25 11.4 11.4 0 0 0 3.6.57 1 1 0 0 1 1 1V20a1 1 0 0 1-1 1A17 17 0 0 1 3 4a1 1 0 0 1 1-1h3.5a1 1 0 0 1 1 1c0 1.25.2 2.45.57 3.57a1 1 0 0 1-.25 1z" fill="var(--orange)"/></svg>
      01632 960418
    </div>
    <div class="contact__line" style="font-size:14.5px">
      <svg width="14" height="11" viewBox="0 0 24 18"><rect width="24" height="18" rx="2" fill="var(--orange)"/><path d="M1 2l11 8 11-8" stroke="#fff" stroke-width="2" fill="none"/></svg>
      enquiries@valteragym.co.uk
    </div>
    <div class="contact__rule"></div>
    <div class="centered">
      <div class="hours__title">Opening hours</div>
      <div class="hours__text">6am - 10pm mon to Fri and<br>7am to 7pm Saturday<br>and Sunday</div>
    </div>
  </div>

  <div class="photo-circle" role="img" aria-label="Photo of a member training in the weights area" style="left:294px;top:427px;width:252px;height:252px;background:radial-gradient(circle at 45% 35%,#8a6a5a,#3a2a2a 70%)"></div>
  <div class="fee-badge abs">Membership<br>fee is<br>£30/month</div>

  <div class="offer abs">If you present this leaflet then<br>there will be no joining fee</div>

  <div class="headline abs">BECOME<br>A MEMBER</div>
  <div class="strapline abs">FITTER STRONGER<br>HEALTHIER</div>

  <div class="abs" style="left:290px;top:685px;width:250px;text-align:center">
    <div class="visit">
      <svg width="16" height="16" viewBox="0 0 24 24" fill="none" stroke="var(--orange)" stroke-width="2"><circle cx="12" cy="12" r="10"/><path d="M2 12h20M12 2c3 3 3 17 0 20M12 2c-3 3-3 17 0 20"/></svg>
      Visit us
    </div>
    <div class="url" style="font-size:15px">www.valteragym.co.uk</div>
  </div>

  <div class="footer-band abs">
    <svg width="11" height="13" viewBox="0 0 24 30"><path d="M12 0a10 10 0 0 0-10 10c0 8 10 20 10 20s10-12 10-20A10 10 0 0 0 12 0zm0 14a4 4 0 1 1 0-8 4 4 0 0 1 0 8z" fill="#fff"/></svg>
    Valtera Gym, Unit 2 Harbour<br>Parade, Linden Avenue, Eastholme, West Sussex, BN99 4QT
  </div>
</section>

<!-- BACK -->
<section class="page page--back">
  <svg class="shapes" width="558" height="789" viewBox="0 0 558 789" role="img" aria-label="Photo of a member using a chest press machine in the strength area">
    <defs>
      <linearGradient id="pressPhoto" x1="0" y1="0" x2="1" y2="1">
        <stop offset="0" stop-color="#7a7570"/>
        <stop offset=".55" stop-color="#3b3536"/>
        <stop offset="1" stop-color="#3f7a3a"/>
      </linearGradient>
    </defs>
    <rect x="0" y="0" width="558" height="380" fill="url(#pressPhoto)"/>
  </svg>
  <svg class="shapes" width="558" height="789" viewBox="0 0 558 789">
    <polygon points="0,683 243,683 279,789 0,789" fill="var(--orange)"/>
  </svg>

  <div class="photo-circle" role="img" aria-label="Photo of a member on a leg machine" style="left:15px;top:234px;width:176px;height:176px;background:radial-gradient(circle at 50% 40%,#8a7060,#3a3038 70%)"></div>
  <div class="photo-circle" role="img" aria-label="Photo of a stair climber in the cardio area" style="left:199px;top:263px;width:160px;height:160px;background:radial-gradient(circle at 50% 40%,#9aa0a8,#3a3a40 75%)"></div>
  <div class="photo-circle" role="img" aria-label="Photo of a member using a shoulder press machine" style="left:367px;top:263px;width:176px;height:176px;background:radial-gradient(circle at 50% 40%,#b0a8a6,#4a3a3a 75%)"></div>

  <div class="pill abs">BENEFITS</div>
  <ul class="benefits abs">
    <li><span class="dot"></span>Wide variety of machines<br>for a full workout</li>
    <li><span class="dot"></span>Great atmosphere</li>
    <li><span class="dot"></span>Friendly and<br>knowledgeable team</li>
    <li><span class="dot"></span>Functional mat area</li>
    <li><span class="dot"></span>Personal trainers available</li>
    <li><span class="dot"></span>Full changing facilities</li>
  </ul>

  <ul class="features abs">
    <li><span class="dot dot--white"></span>Strength machines</li>
    <li><span class="dot dot--white"></span>Cardio machines</li>
    <li><span class="dot dot--white"></span>Functional area</li>
    <li><span class="dot dot--white"></span>Sprung floor mat area</li>
  </ul>

  <div class="brand-mark" style="left:386px;top:631px;width:64px;height:64px;border-color:var(--white)"></div>
  <div class="brand-name" style="left:278px;top:706px;width:280px;text-align:center;font-size:28px;color:var(--white)">VALTERA GYM</div>
  <div class="brand-tag" style="left:278px;top:741px;width:280px;text-align:center;font-size:10px">FITTER | STRONGER | HEALTHIER</div>

  <div class="back-footer abs">
    <div class="visit">
      <svg width="15" height="15" viewBox="0 0 24 24" fill="none" stroke="#fff" stroke-width="2"><circle cx="12" cy="12" r="10"/><path d="M2 12h20M12 2c3 3 3 17 0 20M12 2c-3 3-3 17 0 20"/></svg>
      Visit us
    </div>
    <div class="url">www.valteragym.co.uk</div>
    <div class="address">
      <svg width="8" height="10" viewBox="0 0 24 30"><path d="M12 0a10 10 0 0 0-10 10c0 8 10 20 10 20s10-12 10-20A10 10 0 0 0 12 0zm0 14a4 4 0 1 1 0-8 4 4 0 0 1 0 8z" fill="#fff"/></svg>
      Valtera Gym, Unit<br>2 Harbour Parade, Linden Avenue,<br>Eastholme, West Sussex, BN99 4QT
    </div>
  </div>
</section>

</body>
</html>
```